Verostel business card

Business card for sustainable investment company called "Verostel". Verostel is an exchange platform selling carbon credits between buyers and sellers. Carbon Credits are an environmental commodity for reducing global carbon emissions.

the card should obviously have our logo and the theme should be sustainability/environment mixed with a trading platform.

Contact Information for Business Card

Logo, Name, Title, Phone, Email

Colors
0054AA
0677BA
7BADD7
CADEEF
E8F1F8
0094D4
00A9DD
6FCCEA
C7EBF8
E9F6FB
00AB8E
00BBA5
67D7C9
C6EFE9
E9F9F6
59FF00
82FF00
B8FF75
E3FFCB
F4FFEA

```html
<!DOCTYPE html>
<html lang="en">
<head>
<meta charset="utf-8">
<title>Verostel business card</title>
<link href="https://fonts.googleapis.com/css2?family=Montserrat:wght@400;600;700&family=Roboto+Slab:wght@300&display=swap" rel="stylesheet">
<style>
  :root {
    --page: #e6e7e9;
    --navy: #152a52;
    --blue: #33a9e0;
    --sky: #35bfea;
    --aqua: #6fcfdf;
    --indigo: #4470b8;
    --white: #ffffff;
    --grey: #d5d7db;
  }
  * { margin: 0; padding: 0; box-sizing: border-box; }
  html, body { width: 1200px; height: 900px; overflow: hidden; background: var(--page); }
  .sheet {
    width: 1200px; height: 900px;
    display: flex; flex-direction: column; align-items: center; justify-content: center; gap: 30px;
  }
  .card {
    position: relative; width: 700px; height: 400px; overflow: hidden;
    box-shadow: 0 10px 24px rgba(30, 40, 60, 0.18);
  }
  .card-front {
    background: linear-gradient(30deg, var(--aqua) 0%, var(--sky) 45%, var(--indigo) 100%);
    display: flex; align-items: center; justify-content: center;
  }
  .wordmark {
    font-family: "Montserrat", sans-serif; font-weight: 600;
    letter-spacing: 4px; text-transform: uppercase; white-space: nowrap;
  }
  .card-front .wordmark { color: var(--white); font-size: 70px; }
  .card-back { background: var(--navy); }
  .card-back svg.backdrop { position: absolute; inset: 0; }
  .card-back .wordmark {
    position: absolute; left: 450px; top: 178px; width: 250px; text-align: center;
    color: var(--navy); font-size: 34px; letter-spacing: 2px;
  }
  .contact { position: absolute; left: 0; top: 0; width: 360px; height: 400px; color: var(--white); }
  .contact svg { position: absolute; inset: 0; }
  .person-name {
    position: absolute; left: 124px; top: 94px; white-space: nowrap;
    font-family: "Montserrat", sans-serif; font-weight: 700; font-size: 22px; letter-spacing: 1px;
  }
  .person-title {
    position: absolute; left: 126px; top: 124px; white-space: nowrap;
    font-family: "Montserrat", sans-serif; font-weight: 400; font-size: 18px; letter-spacing: 1px;
  }
  .detail {
    position: absolute; white-space: nowrap;
    font-family: "Roboto Slab", serif; font-weight: 300; font-size: 15px; line-height: 21px;
  }
  .detail-phone { left: 148px; top: 178px; }
  .detail-web { left: 168px; top: 238px; }
  .detail-address { left: 188px; top: 298px; }
</style>
</head>
<body>
<main class="sheet">
  <section class="card card-front">
    <span class="wordmark">Verostel</span>
  </section>

  <section class="card card-back">
    <svg class="backdrop" width="700" height="400" viewBox="0 0 700 400">
      <defs>
        <linearGradient id="mist-fill" x1="0" y1="0" x2="1" y2="1">
          <stop offset="0" stop-color="#ffffff"/>
          <stop offset="1" stop-color="#eef0f3"/>
        </linearGradient>
      </defs>
      <polygon points="240,0 442,0 404,120" fill="var(--blue)"/>
      <polyline points="442,0 372,220 520,400" fill="none" stroke="var(--blue)" stroke-width="8"/>
      <polyline points="456,0 386,220 536,400" fill="none" stroke="var(--white)" stroke-width="5"/>
      <polyline points="352,150 366,262 430,330" fill="none" stroke="var(--grey)" stroke-width="6"/>
      <polygon points="478,0 700,0 700,400 562,400 408,220" fill="url(#mist-fill)"
               role="img" aria-label="Faint triangle pattern background"/>
      <polygon points="562,400 650,400 500,328" fill="var(--blue)"/>
    </svg>

    <span class="wordmark">Verostel</span>

    <div class="contact">
      <svg width="360" height="400" viewBox="0 0 360 400">
        <polyline points="95,140 115,198 135,258 155,318" fill="none" stroke="var(--blue)" stroke-width="3"/>
        <polygon points="75,140 85,123 105,123 115,140 105,157 85,157" fill="var(--blue)"/>
        <circle cx="95" cy="136" r="5" fill="var(--white)"/>
        <path d="M86 150 q9 -11 18 0 z" fill="var(--white)"/>
        <polygon points="96,198 105,183 125,183 134,198 125,213 105,213" fill="var(--navy)" stroke="var(--blue)" stroke-width="3"/>
        <path d="M108 195 q7 -6 14 0 v3 h-3 v-2 h-8 v2 h-3 z M109 200 h12 v6 h-12 z" fill="var(--white)"/>
        <polygon points="116,258 125,243 145,243 154,258 145,273 125,273" fill="var(--navy)" stroke="var(--blue)" stroke-width="3"/>
        <circle cx="135" cy="258" r="7" fill="none" stroke="var(--white)" stroke-width="1.4"/>
        <ellipse cx="135" cy="258" rx="3" ry="7" fill="none" stroke="var(--white)" stroke-width="1.2"/>
        <line x1="128" y1="258" x2="142" y2="258" stroke="var(--white)" stroke-width="1.2"/>
        <polygon points="136,318 145,303 165,303 174,318 165,333 145,333" fill="var(--navy)" stroke="var(--blue)" stroke-width="3"/>
        <path d="M155 327 l-5 -8 a6 6 0 1 1 10 0 z" fill="var(--white)"/>
        <circle cx="155" cy="315" r="2" fill="var(--navy)"/>
      </svg>
      <div class="person-name">MARLO FENWICK</div>
      <div class="person-title">Founder</div>
      <div class="detail detail-phone">000 4821 3907<br>000 4821 3908</div>
      <div class="detail detail-web">hello@verostel.com<br>www.verostel.com</div>
      <div class="detail detail-address">27, 2nd Floor,<br>Elm Row, NY 410592</div>
    </div>
  </section>
</main>
</body>
</html>
```